RK Tannery Construction Inc.

Design a new business card for our construction company
To be removed from current card:
Delete 25 years
Delete Tenant fit up Renovations section

```html
<!DOCTYPE html>
<html lang="en">
<head>
<meta charset="utf-8">
<title>RK Tannery Construction Inc. – Business Card</title>
<link href="https://fonts.googleapis.com/css2?family=Montserrat:wght@400;500;700&display=swap" rel="stylesheet">
<style>
  :root {
    --purple: #532d7a;
    --teal: #1f7a6b;
    --ink: #555555;
    --white: #ffffff;
    --backdrop: #8c8c8c;
  }
  * { box-sizing: border-box; margin: 0; padding: 0; }
  html, body { width: 1200px; height: 801px; overflow: hidden; }
  body {
    background: var(--backdrop);
    font-family: "Montserrat", sans-serif;
    position: relative;
  }
  .card {
    position: absolute;
    top: 252px;
    width: 520px;
    height: 297px;
    border-radius: 16px;
    overflow: hidden;
  }
  .card-front { left: 50px; background: var(--white); }
  .card-back { left: 630px; background: var(--purple); }

  /* company name placeholder */
  .company {
    position: absolute;
    display: flex;
    align-items: center;
    gap: 10px;
    font-weight: 700;
    line-height: 1;
  }
  .company-mark { width: 14px; height: 14px; flex: none; }
  .card-front .company { left: 40px; top: 52px; color: var(--purple); font-size: 24px; }
  .card-front .company-mark { background: var(--purple); }
  .card-back .company { left: 0; right: 0; top: 110px; justify-content: center; color: var(--white); font-size: 28px; }
  .card-back .company-mark { background: var(--white); }

  /* front details */
  .holder { position: absolute; left: 40px; top: 150px; }
  .holder-name { color: var(--purple); font-weight: 700; font-size: 17px; letter-spacing: 0.3px; }
  .holder-address { color: var(--ink); font-size: 13px; line-height: 1.45; margin-top: 8px; }

  .divider { position: absolute; left: 268px; top: 140px; width: 1px; height: 78px; background: var(--purple); }

  .contacts { position: absolute; left: 284px; top: 138px; list-style: none; }
  .contacts li { display: flex; align-items: center; gap: 8px; color: var(--ink); font-size: 12.5px; line-height: 20px; }
  .contacts svg { width: 11px; height: 11px; fill: var(--teal); flex: none; }

  .services-band {
    position: absolute; left: 0; right: 0; bottom: 0; height: 46px;
    background: var(--purple); color: var(--white);
    display: flex; align-items: center; justify-content: center;
    font-size: 14px; font-weight: 500; letter-spacing: 0.4px;
  }

  /* back */
  .sectors {
    position: absolute; left: 0; right: 0; top: 222px; text-align: center;
    color: var(--white); font-size: 16px; font-weight: 500; letter-spacing: 0.6px;
  }
</style>
</head>
<body>

<section class="card card-front" aria-label="Business card front">
  <div class="company"><span class="company-mark"></span>RK Tannery Construction Inc.</div>

  <div class="holder">
    <p class="holder-name">MARC TANNERY</p>
    <p class="holder-address">1280 Fieldstone Rd., Suite 100<br>Ottawa, ON K1J 4B7</p>
  </div>

  <div class="divider"></div>

  <ul class="contacts">
    <li><svg viewBox="0 0 12 12" aria-hidden="true"><path d="M3 0h6a1 1 0 0 1 1 1v10a1 1 0 0 1-1 1H3a1 1 0 0 1-1-1V1a1 1 0 0 1 1-1zm0 1.5v8h6v-8z"/></svg>613-555-0142</li>
    <li><svg viewBox="0 0 12 12" aria-hidden="true"><path d="M2.5 0.5l2 2.5-1.2 1.4a7 7 0 0 0 4.3 4.3L9 7.5l2.5 2-1.2 2C5 11.5 0.5 7 0.5 1.7z"/></svg>613-555-0187 ext. 221</li>
    <li><svg viewBox="0 0 12 12" aria-hidden="true"><path d="M0 2h12v8H0zm1 1v.4l5 3.2 5-3.2V3z"/></svg>marc@rktanneryconst.ca</li>
    <li><svg viewBox="0 0 12 12" aria-hidden="true"><circle cx="6" cy="6" r="6"/></svg>www.rktanneryconst.ca</li>
  </ul>

  <div class="services-band">Turn Key Operations &nbsp;•&nbsp; Project Management</div>
</section>

<section class="card card-back" aria-label="Business card back">
  <div class="company"><span class="company-mark"></span>RK Tannery Construction Inc.</div>
  <p class="sectors">OFFICE &nbsp;•&nbsp; RETAIL &nbsp;•&nbsp; INSTITUTIONAL</p>
</section>

</body>
</html>
```